Startup Burlesque Dance Company needs logo and website

Hello designers,
We need a logo design and a website design. The company name is "Vespera Lumina". This is a rough cut of one of the company's shows: http://clipvault.example/q7TrnoPaLk2
The design will be for a startup Burlesque dance company. The logo and website should have a simple, retro, vintage "black and white" movie feel to it. The primary purpose for the site is for marketing the dance services, highlighting pictures and video of the show(s). There will be seven basic web pages.
• Home
• About
• Shows
• Company
• Gallery
• Promo Reel
• Contact
The following links are two examples of sites we like, but since this is a competitor, the design should not be identical. It should only serve as an example of the requested style.
http://pemberlysilkrevue.example/index.cfm
http://www.brightwickcarnival.example/
In Summary, we will need the following:
1. Logo (example of ones we like are attached in Word file)
2. Web Site Design
3. Stationary ready design for business cards and letterhead
Please design to the following screen size & resolution: 1024 x 768
Reason: Decision maker has been traveling on business so our team has not been able to meet with her.
Target Market(s)
Male and Female, 21-45 years of age
Industry/Entity Type
Marketing
Look and feel

```html
<!DOCTYPE html>
<html lang="en">
<head>
<meta charset="utf-8">
<title>Vespera Lumina — Home</title>
<link href="https://fonts.googleapis.com/css2?family=Pathway+Gothic+One&family=Tinos:wght@400;700&display=swap" rel="stylesheet">
<style>
  :root {
    --wall: #e4e4e4;
    --wall-dark: #cfcfcf;
    --ink: #111111;
    --panel: #1c1c1c;
    --accent: #d0353a;
    --paper: #ffffff;
    --muted: #9a9a9a;
    --line: #2a2a2a;
  }
  * { box-sizing: border-box; margin: 0; padding: 0; }
  html, body { width: 1200px; height: 1012px; overflow: hidden; }
  body {
    position: relative;
    background: radial-gradient(ellipse at 40% 30%, #f0f0f0 0%, var(--wall) 55%, var(--wall-dark) 100%);
    font-family: "Pathway Gothic One", "Arial Narrow", sans-serif;
    color: var(--ink);
  }
  .page-column {
    position: absolute; left: 168px; top: 0; width: 864px; height: 940px;
    background: linear-gradient(180deg, rgba(255,255,255,.35), rgba(255,255,255,.15));
    box-shadow: -3px 0 6px rgba(0,0,0,.25), 3px 0 6px rgba(0,0,0,.25);
  }
  .abs { position: absolute; }

  /* brand */
  .brand {
    left: 197px; top: 40px; width: 240px;
    font-size: 44px; line-height: 44px; letter-spacing: 1px; color: var(--ink);
    display: flex; align-items: center; gap: 12px;
  }
  .brand-dot { width: 16px; height: 16px; border-radius: 50%; background: var(--ink); flex: none; }
  .brand-name { display: block; }

  /* contact strip */
  .call-us { left: 574px; top: 26px; font-size: 25px; letter-spacing: .5px; }
  .call-us .phone { font-family: "Tinos", serif; font-weight: 700; color: var(--accent); font-size: 22px; }
  .strip-divider { left: 784px; top: 20px; width: 2px; height: 44px; background: #444; }
  .follow-us { left: 805px; top: 26px; font-size: 25px; letter-spacing: .5px; }
  .social { top: 26px; width: 32px; height: 32px; border-radius: 6px;
    background: linear-gradient(180deg, #8a8f99, #4f545d); box-shadow: 0 1px 2px rgba(0,0,0,.4); }

  /* navigation */
  .main-nav a {
    position: absolute; top: 87px; height: 41px;
    background: var(--ink); color: #f2f2f2; text-decoration: none;
    font-size: 18px; line-height: 41px; text-align: center; letter-spacing: .5px;
  }
  .main-nav a.is-active { background: var(--accent); }

  /* hero */
  .hero-frame { left: 183px; top: 164px; width: 834px; height: 382px; background: var(--paper);
    box-shadow: 0 22px 18px -12px rgba(0,0,0,.45); }
  .hero-photo { left: 190px; top: 171px; width: 820px; height: 367px;
    background: radial-gradient(ellipse at 55% 45%, #6b6e70 0%, #3c3e40 55%, #222 100%); }
  .hero-photo::after { content: ""; position: absolute; left: 36%; top: 22%; width: 24%; height: 20%;
    background: radial-gradient(ellipse, rgba(217,90,40,.55), transparent 70%); }

  /* welcome */
  .welcome { left: 183px; top: 604px; width: 299px; height: 288px; background: var(--panel); color: #f3f3f3; padding: 16px 16px 0 16px; }
  .welcome h2 { font-weight: 400; font-size: 38px; line-height: 42px; letter-spacing: .5px; margin-bottom: 10px; }
  .welcome .lead { font-family: "Tinos", serif; font-size: 14.5px; line-height: 16.5px; margin-bottom: 14px; }
  .welcome .body { font-family: "Tinos", serif; font-size: 12px; line-height: 14.6px; }

  /* most popular */
  .section-title { left: 506px; top: 596px; font-size: 40px; line-height: 44px; letter-spacing: .5px; }
  .title-rule { left: 498px; top: 641px; width: 519px; height: 5px; border-top: 1px solid var(--line); border-bottom: 1px solid var(--line); }
  .slider-arrows { left: 957px; top: 603px; }
  .video { width: 242px; height: 167px; background: #000; overflow: hidden; }
  .video-shot { position: absolute; left: 0; top: 0; width: 100%; height: 146px; }
  .shot-stage { background: radial-gradient(ellipse at 50% 85%, #b5531d 0%, #5a2a12 35%, #080808 70%); }
  .shot-red { background: radial-gradient(ellipse at 45% 50%, #b3293b 0%, #4a1420 35%, #050505 72%); }
  .player-bar { position: absolute; left: 0; bottom: 0; width: 100%; height: 21px; background: #1e1e1e; }
  .player-bar .track { position: absolute; left: 0; top: 0; width: 100%; height: 3px; background: #555; }
  .player-bar .time { position: absolute; left: 47px; top: 7px; font-family: Arial, sans-serif; font-size: 6px; color: #bbb; }

  .more-rule { left: 498px; top: 871px; width: 519px; height: 5px; border-top: 1px solid var(--line); border-bottom: 1px solid var(--line); }
  .view-more { left: 721px; top: 861px; width: 82px; height: 31px; background: var(--accent); color: #fff;
    font-size: 16px; line-height: 31px; text-align: center; text-decoration: none; }

  /* footer */
  .site-footer { position: absolute; left: 0; top: 940px; width: 1200px; height: 72px; background: var(--panel); color: #eee; text-align: center; }
  .footer-nav { position: absolute; top: 14px; width: 100%; font-size: 17px; letter-spacing: .5px; }
  .footer-nav a { color: #eee; text-decoration: none; }
  .footer-nav .sep { color: #888; margin: 0 20px; }
  .copyright { position: absolute; top: 38px; width: 100%; font-size: 13px; letter-spacing: .3px; color: #ddd; }
  .copyright strong { color: #fff; font-weight: 400; }
</style>
</head>
<body>
  <div class="page-column"></div>

  <header>
    <div class="abs brand"><span class="brand-name">Vespera Lumina</span><span class="brand-dot"></span></div>

    <div class="abs call-us">CALL US - <span class="phone">555 014 276</span></div>
    <div class="abs strip-divider"></div>
    <div class="abs follow-us">FOLLOW US</div>
    <a class="abs social" style="left:908px" href="#" aria-label="Social profile one"></a>
    <a class="abs social" style="left:948px" href="#" aria-label="Social profile two"></a>
    <a class="abs social" style="left:985px" href="#" aria-label="Social profile three"></a>

    <nav class="main-nav">
      <a class="is-active" href="#" style="left:494px;width:61px">HOME</a>
      <a href="#" style="left:562px;width:60px">ABOUT</a>
      <a href="#" style="left:629px;width:61px">SHOWS</a>
      <a href="#" style="left:697px;width:70px">COMPANY</a>
      <a href="#" style="left:774px;width:70px">GALLERY</a>
      <a href="#" style="left:851px;width:80px">PROMO REEL</a>
      <a href="#" style="left:938px;width:79px">CONTACT</a>
    </nav>
  </header>

  <main>
    <div class="abs hero-frame"></div>
    <div class="abs hero-photo" role="img" aria-label="Street dancer in an orange top and jeans mid-move against a grey wall"></div>

    <section class="abs welcome">
      <h2>WELCOME !</h2>
      <p class="lead">Lorem Ipsum is simply dummy text of the printing and typesetting industry. Lorem Ipsum has been the industry's standard dummy text ever since the 1500s.</p>
      <p class="body">Lorem Ipsum is simply dummy text of the printing and typesetting industry. Lorem Ipsum has been the industry's standard dummy text ever since the 1500s, when an unknown printer took a galley of type and scrambled it to make a type specimen book. It has survived not only five centuries, but also the leap into electronic typesetting, remaining essentially unchanged.</p>
    </section>

    <h2 class="abs section-title" style="font-weight:400">MOST POPULAR</h2>
    <svg class="abs slider-arrows" width="60" height="28" viewBox="0 0 60 28" aria-label="Previous and next">
      <path d="M22 2 L8 14 L22 26 L16 26 L2 14 L16 2 Z" fill="#1a1a1a"/>
      <path d="M36 2 L50 14 L36 26 L42 26 L56 14 L42 2 Z" fill="#1a1a1a"/>
    </svg>
    <div class="abs title-rule"></div>

    <div class="abs video" style="left:507px;top:669px">
      <div class="video-shot shot-stage" role="img" aria-label="Couples dancing on a warmly lit stage"></div>
      <div class="player-bar">
        <div class="track"></div>
        <svg class="abs" style="left:10px;top:8px" width="30" height="8" viewBox="0 0 30 8"><path d="M0 0 L6 4 L0 8 Z" fill="#bbb"/><rect x="20" y="2" width="3" height="4" fill="#bbb"/><path d="M23 2 L27 0 L27 8 L23 6 Z" fill="#bbb"/></svg>
        <span class="time">0:00 / 0:32</span>
        <svg class="abs" style="left:170px;top:7px" width="66" height="8" viewBox="0 0 66 8"><circle cx="4" cy="4" r="3" fill="#bbb"/><circle cx="20" cy="4" r="3" fill="#bbb"/><rect x="32" y="1" width="9" height="6" fill="none" stroke="#bbb"/><rect x="46" y="1" width="9" height="6" fill="none" stroke="#bbb"/><rect x="58" y="0" width="8" height="8" fill="none" stroke="#bbb"/></svg>
      </div>
    </div>

    <div class="abs video" style="left:777px;top:669px">
      <div class="video-shot shot-red" role="img" aria-label="Dancers in red and pink dresses leaping on a dark stage"></div>
      <div class="player-bar">
        <div class="track"></div>
        <svg class="abs" style="left:10px;top:8px" width="30" height="8" viewBox="0 0 30 8"><path d="M0 0 L6 4 L0 8 Z" fill="#bbb"/><rect x="20" y="2" width="3" height="4" fill="#bbb"/><path d="M23 2 L27 0 L27 8 L23 6 Z" fill="#bbb"/></svg>
        <span class="time">0:00 / 0:32</span>
        <svg class="abs" style="left:170px;top:7px" width="66" height="8" viewBox="0 0 66 8"><circle cx="4" cy="4" r="3" fill="#bbb"/><circle cx="20" cy="4" r="3" fill="#bbb"/><rect x="32" y="1" width="9" height="6" fill="none" stroke="#bbb"/><rect x="46" y="1" width="9" height="6" fill="none" stroke="#bbb"/><rect x="58" y="0" width="8" height="8" fill="none" stroke="#bbb"/></svg>
      </div>
    </div>

    <div class="abs more-rule"></div>
    <a class="abs view-more" href="#">VIEW MORE</a>
  </main>

  <footer class="site-footer">
    <div class="footer-nav">
      <a href="#">HOME</a><span class="sep">|</span><a href="#">ABOUT</a><span class="sep">|</span><a href="#">SHOWS</a><span class="sep">|</span><a href="#">COMPANY</a><span class="sep">|</span><a href="#">GALLERY</a><span class="sep">|</span><a href="#">PROMO REEL</a><span class="sep">|</span><a href="#">CONTACT</a>
    </div>
    <div class="copyright">COPYRIGHT © <strong>VESPERA LUMINA</strong> 2013. ALL RIGHT RESERVED</div>
  </footer>
</body>
</html>
```